Business Card for Flight Instructor/Commercial Pilot

I need a business card for myself as a Flight Instructor. I'm a certificated flight instructor at a local flight school in St Paul, MN and want to have a business card that I can give out both to prospective students and also to prospective employers in commercial/business aviation. The business card should have a few elements to it (my name, my position, and my ZRT certifications:
Dorian Welkes, MBA
Flight Instructor
CFI, CFII, AGI, IGI
Then lastly, I'd like it to include my phone number for calls or texts, my email address, and my Corvanet url. I'll provide all of these at a later point.

If we can include some kind of aviation graphic, that's great, but I don't currently have a logo and I don't necessarily need one, so don't feel like a logo is required here, it's not. I'm but I'm open to whatever you might put together. But I honestly don't need a logo, just good design with a simple graphic element to draw a little interest.
I'd also like to add a short tag line. A few ideas I have are:
- Fly Smart. Stay Humble. Never Stop Learning.
- Train smart. Fly safe. Have fun.
- Master the craft. Enjoy the flight.

For the back side, I'm open to ideas on what to put there. maybe the tagline could go there, or a QR code for my Corvanet page, or maybe something else.

Target audience is both prospective students who are interested in learning to fly (or adding more ratings) and commercial aviation companies that could be potential employer for me in commercial aviation. Trying to portray a sense of professionalism, trust, and high level of competency.

The business card doesn’t have to be standard (rectangular with square corners) and I’m open to suggestions for based on the design.
Lastly, I just don't want the design created by AI.
Let me know if you need any further info. Thanks!

```html
<!DOCTYPE html>
<html lang="en">
<head>
<meta charset="utf-8">
<title>Dorian Welkes — Business Card</title>
<link href="https://fonts.googleapis.com/css2?family=Montserrat:wght@300;400;500;600&display=swap" rel="stylesheet">
<style>
  :root {
    --navy: #0b1a2e;
    --navy-mono: #13294a;
    --ink: #1a2740;
    --paper: #ffffff;
    --stage: #ffffff;
    --text-light: #eef1f6;
    --text-muted: #b9c3d3;
    --dial: #ececec;
  }
  * { box-sizing: border-box; margin: 0; padding: 0; }
  html, body {
    width: 1200px; height: 1200px; overflow: hidden;
    background: var(--stage);
    font-family: "Montserrat", sans-serif;
  }
  .sheet {
    position: relative; width: 1200px; height: 1200px;
    display: flex; align-items: center; justify-content: center; gap: 56px;
  }
  .card {
    position: relative; width: 540px; height: 348px; overflow: hidden;
    box-shadow: 0 14px 30px rgba(0,0,0,0.35);
  }
  .card--front { background: var(--navy); color: var(--text-light); }
  .card--back { background: var(--paper); color: var(--ink); }

  .monogram {
    position: absolute; left: 68px; top: -62px;
    font-weight: 300; font-size: 440px; line-height: 1;
    letter-spacing: -10px; color: var(--navy-mono);
    white-space: nowrap; user-select: none;
  }
  .identity {
    position: absolute; left: 0; right: 0; top: 162px; text-align: center;
  }
  .card--back .identity { top: 158px; }
  .identity__name {
    font-weight: 500; font-size: 19px; letter-spacing: 3.2px;
  }
  .identity__role {
    margin-top: 6px; font-weight: 500; font-size: 10.5px; letter-spacing: 2.4px;
  }
  .identity__certs {
    margin-top: 5px; font-weight: 400; font-size: 7px; letter-spacing: 1.6px;
    color: var(--text-muted);
  }
  .card--back .identity__certs { color: #6b7588; }

  .contact {
    position: absolute; bottom: 22px; font-size: 9.5px; line-height: 1.3;
    letter-spacing: 0.4px; color: var(--text-light);
  }
  .contact--left { left: 34px; }
  .contact--right { right: 38px; text-align: right; }

  .dial {
    position: absolute; left: 50%; top: 50%; width: 340px; height: 340px;
    transform: translate(-50%, -50%);
  }
</style>
</head>
<body>
<main class="sheet">
  <section class="card card--front" aria-label="Card front">
    <div class="monogram" aria-hidden="true">DW</div>
    <div class="identity">
      <h1 class="identity__name">DORIAN WELKES, MBA</h1>
      <p class="identity__role">FLIGHT INSTRUCTOR</p>
      <p class="identity__certs">CFI · CFII · AGI · IGI</p>
    </div>
    <div class="contact contact--left">
      <p>(111) 111-1111</p>
      <p>name.lastname@dorianwelkes.com</p>
      <p>dorianwelkes.com</p>
    </div>
    <div class="contact contact--right">
      <p>1111 address address</p>
      <p>address placeholder</p>
      <p>111111 postal code</p>
    </div>
  </section>

  <section class="card card--back" aria-label="Card back">
    <svg class="dial" viewBox="0 0 340 340" role="img" aria-label="Faint heading indicator dial graphic">
      <defs>
        <radialGradient id="dialTone" cx="50%" cy="50%" r="50%">
          <stop offset="0.62" stop-color="#ffffff" stop-opacity="0"/>
          <stop offset="0.72" stop-color="#f1f1f1"/>
          <stop offset="0.95" stop-color="#f4f4f4"/>
          <stop offset="1" stop-color="#ffffff" stop-opacity="0"/>
        </radialGradient>
      </defs>
      <circle cx="170" cy="170" r="170" fill="url(#dialTone)"/>
    </svg>
    <div class="identity">
      <h1 class="identity__name">DORIAN WELKES, MBA</h1>
      <p class="identity__role">FLIGHT INSTRUCTOR</p>
      <p class="identity__certs">CFI · CFII · AGI · IGI</p>
    </div>
  </section>
</main>
</body>
</html>
```